Special release wine label

Marrow Creek Vineyards is a small premium wine producer in the Barossa - South Australia. We are a five star rated winery, producing exceptional wines true to variety, region and house style. We have a very special parcel of wine that we wish to release as an exclusive wine. Visit www.marrowcreekvineyards.com.au for further feel.

The wine will be called Marrow Creek Vineyards, 2012, The Quiet Harvest Shiraz - Cabernet.

The wine can be bottled in either a burgundy or Bordeaux shaped bottle

Industry/Entity Type

House

```html
<!DOCTYPE html>
<html lang="en">
<head>
<meta charset="utf-8">
<title>Marrow Creek Vineyards – The Quiet Harvest 2012</title>
<link rel="stylesheet" href="https://fonts.googleapis.com/css2?family=Cinzel:wght@600;700&family=Arimo:wght@700&display=swap">
<style>
  :root {
    --backdrop-top: #b9c9dc;
    --backdrop-bottom: #e6ebf1;
    --label-orange: #f8aa5c;
    --collar-deep: #f0661a;
    --collar-light: #fdd9b8;
    --rule-grey: #b3b0b2;
    --ink-dark: #1d1611;
    --panel-cream: #f4f1ea;
    --panel-tan: #a58f78;
    --panel-brown: #3a2b20;
    --scene-light: #d8d2c6;
    --scene-mid: #8a857c;
    --type-white: #ffffff;
  }
  * { margin: 0; padding: 0; box-sizing: border-box; }
  html, body { width: 1200px; height: 3364px; overflow: hidden; }
  body {
    position: relative;
    background: linear-gradient(180deg, var(--backdrop-top) 0%, var(--backdrop-bottom) 100%);
    font-family: "Cinzel", "Times New Roman", serif;
  }
  .neck-collar {
    position: absolute;
    left: 0; top: 0;
    width: 1200px; height: 3364px;
  }
  .body-label {
    position: absolute;
    left: 224px; top: 1612px;
    width: 757px; height: 1290px;
    background: var(--label-orange);
    border-radius: 10px;
    display: flex;
    flex-direction: column;
    align-items: center;
  }
  .wine-title {
    margin-top: 68px;
    text-align: center;
    color: var(--ink-dark);
    font-weight: 700;
    font-size: 46px;
    line-height: 72px;
    letter-spacing: 1px;
  }
  .rule {
    position: absolute;
    left: 64px;
    width: 623px;
    height: 16px;
    background: var(--rule-grey);
  }
  .rule--top { top: 304px; }
  .rule--bottom { top: 1232px; }
  .brand-panel {
    position: absolute;
    left: 84px; top: 351px;
    width: 589px; height: 813px;
    border-radius: 0 0 70px 70px;
    background: linear-gradient(180deg, var(--panel-cream) 0%, var(--panel-cream) 35%, var(--panel-tan) 62%, var(--panel-brown) 88%, var(--panel-brown) 100%);
    display: flex;
    flex-direction: column;
    align-items: center;
  }
  .brand-name {
    margin-top: 28px;
    color: var(--ink-dark);
    font-weight: 600;
    font-size: 58px;
    letter-spacing: 2px;
    line-height: 80px;
  }
  .estate-scene {
    margin-top: 30px;
    width: 533px; height: 449px;
    background: radial-gradient(ellipse at 50% 60%, var(--scene-mid) 0%, var(--scene-light) 65%, var(--panel-cream) 100%);
    opacity: 0.85;
  }
  .brand-descriptor {
    margin-top: 52px;
    color: var(--type-white);
    font-weight: 600;
    font-size: 60px;
    letter-spacing: 8px;
    line-height: 70px;
  }
  .vintage {
    margin-top: 8px;
    color: var(--type-white);
    font-family: "Arimo", Arial, sans-serif;
    font-weight: 700;
    font-size: 74px;
    letter-spacing: 3px;
    line-height: 84px;
  }
</style>
</head>
<body>
  <svg class="neck-collar" viewBox="0 0 1200 3364" aria-hidden="true">
    <defs>
      <linearGradient id="collar-fill" x1="0" y1="0" x2="0" y2="1">
        <stop offset="0" stop-color="var(--collar-deep)"/>
        <stop offset="0.55" stop-color="#f68c4a"/>
        <stop offset="1" stop-color="var(--collar-light)"/>
      </linearGradient>
    </defs>
    <path d="M280 1165 Q330 1050 420 1000 Q520 1030 598 1150 Q680 1030 776 1000 Q866 1050 911 1165 Q780 1200 700 1270 Q640 1310 598 1346 Q556 1310 496 1270 Q416 1200 280 1165 Z"
          fill="url(#collar-fill)" stroke="#ffffff" stroke-width="3"/>
  </svg>

  <section class="body-label">
    <h1 class="wine-title">The Quiet Harvest<br>Shiraz - Cabernet</h1>
    <div class="rule rule--top"></div>
    <div class="brand-panel">
      <p class="brand-name">Marrow Creek</p>
      <div class="estate-scene" role="img" aria-label="Pen sketch of the homestead cottage framed by tall palm trees and garden"></div>
      <p class="brand-descriptor">Vineyards</p>
      <p class="vintage">2.0.1.2</p>
    </div>
    <div class="rule rule--bottom"></div>
  </section>
</body>
</html>
```